Coastal waterside shopping complex needs a billboard sign

"Harbor Quay" is the name of a building which comprises 4 shops in a coastal waterside location. We need a 2440mm (Wide) x 1100mm (High) "Harbor Quay" billboard design that will fit with the coastal theme but is modern and contemporary, positioning the building as a high class mini shopping complex.

The photo below is for reference only. We only need a design for the "Harbor Quay" sign.

The end product will need to be an EPS scalable vector file.

Industry/Entity Type

Shopping

```html
<!DOCTYPE html>
<html lang="en">
<head>
<meta charset="utf-8">
<title>Harbor Quay – Billboard Sign</title>
<link rel="stylesheet" href="https://fonts.googleapis.com/css2?family=Yellowtail&display=swap">
<style>
  :root {
    --backdrop: #e9ecee;
    --frame-teal: #1b94b8;
    --frame-line: #5cc0dc;
    --sky-top: #7fd0ee;
    --sky-glow: #f4fbfd;
    --sky-mid: #a8def2;
    --cloud-white: #f5fbfe;
    --horizon: #1ea7d6;
    --sea-deep: #3cb8e0;
    --sea-light: #d9f2fb;
    --title-teal: #0f7d98;
    --title-edge: #ffffff;
  }
  * { margin: 0; padding: 0; box-sizing: border-box; }
  html, body {
    width: 1200px;
    height: 794px;
    overflow: hidden;
    background: var(--backdrop);
  }
  .canvas {
    position: relative;
    width: 1200px;
    height: 794px;
  }
  .billboard {
    position: absolute;
    left: 40px;
    top: 144px;
    width: 1120px;
    height: 506px;
    background: var(--frame-teal);
    padding: 22px;
    box-shadow: 0 6px 18px rgba(0, 0, 0, 0.25);
  }
  .billboard-inner {
    position: relative;
    width: 100%;
    height: 100%;
    overflow: hidden;
  }
  .frame-rule {
    position: absolute;
    inset: 7px;
    border: 2px solid var(--frame-line);
    pointer-events: none;
  }
  .coastal-scene {
    position: absolute;
    inset: 0;
    background:
      radial-gradient(ellipse 38% 55% at 50% 12%, var(--sky-glow) 0%, rgba(244, 251, 253, 0) 100%),
      radial-gradient(ellipse 60% 22% at 30% 66%, var(--cloud-white) 0%, rgba(245, 251, 254, 0) 100%),
      radial-gradient(ellipse 45% 20% at 80% 64%, var(--cloud-white) 0%, rgba(245, 251, 254, 0) 100%),
      linear-gradient(180deg,
        var(--sky-top) 0%,
        var(--sky-mid) 45%,
        var(--cloud-white) 68%,
        var(--horizon) 73%,
        var(--sea-deep) 78%,
        var(--sea-light) 100%);
  }
  .sign-title {
    position: absolute;
    inset: 0;
    width: 100%;
    height: 100%;
  }
  .sign-title text {
    font-family: "Yellowtail", cursive;
    font-size: 210px;
    fill: var(--title-teal);
    stroke: var(--title-edge);
    stroke-width: 12px;
    stroke-linejoin: round;
    paint-order: stroke fill;
  }
</style>
</head>
<body>
  <main class="canvas">
    <section class="billboard">
      <div class="billboard-inner">
        <div class="coastal-scene" role="img" aria-label="Illustrated seascape: sun rays in a pale blue sky, white clouds along the horizon, calm turquoise sea with gulls"></div>
        <svg class="sign-title" viewBox="0 0 1076 462" aria-label="Harbor Quay">
          <defs>
            <filter id="title-shadow" x="-10%" y="-20%" width="120%" height="140%">
              <feDropShadow dx="4" dy="7" stdDeviation="5" flood-color="#0b4f63" flood-opacity="0.35"/>
            </filter>
          </defs>
          <text x="548" y="295" text-anchor="middle" textLength="880" lengthAdjust="spacingAndGlyphs" filter="url(#title-shadow)">Harbor Quay</text>
        </svg>
        <div class="frame-rule"></div>
      </div>
    </section>
  </main>
</body>
</html>
```